The Quiet Pantry Method: Reshape Your Habits Around Meals in Only 30 Days

I want a book cover for a paperback non-fiction book 30 day challenge to transform you relationship with your food, diet and lifestyle for longterm health and vitality. I would like to incorporate two photos on the front cover, one of a Greek salad and one of me the author. I have uploaded the four photos. Use which of each pair you think best. Because of my name, I want the photo on the cover. Otherwise folks assume Marla is a guy.
I am looking at best selling health books and they seem to be on the lighter side color-wise, with horizontal design. Green and orange seem to work most often, though my logo is a bluish turquoise (https://marlavoskin.com). I would imagine a light background, clear simple fonts. Looking forward to your designs!

Target Market(s)

Women around 35-40 confused by conflicting nutrition information but dedicated to better health haelthy

Industry/Entity Type

nutrition and wellness

Font styles to use
Serif

Colors
00AB8E
00BBA5
67D7C9
C6EFE9
E9F9F6
F0912C
F2A743
F7CA91
FBE8D2
FDF5EE
EE7325
F08F49
F5BC92
FAE3D3
FDF4ED

Requirements
Must have
• Clear simple look with room for an endorsement
Nice to have
• Hints of natural scenes and happy places
Should not have
• Dark or ominous feel

```html
<!DOCTYPE html>
<html lang="en">
<head>
<meta charset="utf-8">
<title>The Quiet Pantry Method — Cover Wrap</title>
<link href="https://fonts.googleapis.com/css2?family=Noticia+Text:wght@400;700&display=swap" rel="stylesheet">
<style>
  :root {
    --teal-deep: #17957a;
    --teal-base: #1f9e80;
    --teal-soft: #3fb395;
    --teal-mist: #7fcdb6;
    --ink-light: #ffffff;
    --ink-pale: #d9f3ea;
    --salad-dark: #5d4a3c;
    --salad-warm: #9a7a5c;
    --salad-green: #6a9a45;
    --portrait-warm: #c9a27e;
    --portrait-dark: #4a3128;
  }
  * { margin: 0; padding: 0; box-sizing: border-box; }
  html, body { width: 1200px; height: 848px; overflow: hidden; background: var(--teal-base); }
  .cover-wrap {
    position: relative; width: 1200px; height: 848px;
    background: var(--teal-base);
    font-family: "Noticia Text", Georgia, serif;
    color: var(--ink-light);
  }
  .back-cover {
    position: absolute; left: 0; top: 0; width: 570px; height: 848px;
    background:
      radial-gradient(ellipse 260px 360px at 270px 360px, var(--teal-mist) 0%, rgba(127,205,182,0) 70%),
      linear-gradient(160deg, var(--teal-soft), var(--teal-deep));
  }
  .spine {
    position: absolute; left: 570px; top: 0; width: 56px; height: 848px;
    background: var(--teal-base);
    display: flex; align-items: center; justify-content: center;
  }
  .spine-text {
    writing-mode: vertical-rl;
    display: flex; justify-content: space-between;
    height: 808px;
    font-size: 17px; letter-spacing: 1.5px; text-transform: uppercase;
    color: var(--ink-pale);
  }
  .front-cover {
    position: absolute; left: 626px; top: 0; width: 574px; height: 848px;
    background:
      radial-gradient(ellipse 240px 300px at 180px 640px, rgba(127,205,182,0.55) 0%, rgba(127,205,182,0) 70%),
      var(--teal-base);
  }
  .salad-photo {
    position: absolute; left: 0; top: 52px; width: 574px; height: 388px;
    background:
      radial-gradient(circle 130px at 380px 160px, var(--salad-green) 0%, rgba(106,154,69,0) 100%),
      radial-gradient(circle 70px at 140px 280px, #e9e4d6 0%, rgba(233,228,214,0) 100%),
      linear-gradient(135deg, var(--salad-warm), var(--salad-dark));
  }
  .author-photo {
    position: absolute; left: 374px; top: 322px; width: 136px; height: 134px;
    background: linear-gradient(160deg, var(--portrait-dark), var(--portrait-warm) 70%, #e3cfb2);
  }
  .title-block { position: absolute; left: 30px; top: 476px; width: 520px; }
  .series-line {
    font-size: 15px; font-weight: 700; letter-spacing: 1px; text-transform: uppercase;
  }
  .main-title {
    margin-top: 14px; font-size: 33px; font-weight: 400; line-height: 1.2;
  }
  .author-name {
    position: absolute; left: 0; width: 574px; top: 778px; text-align: center;
    font-size: 15px; letter-spacing: 2.5px; text-transform: uppercase;
  }
</style>
</head>
<body>
  <div class="cover-wrap">
    <section class="back-cover" role="img" aria-label="Soft green-toned photo of a woman with flowing hair, eyes closed"></section>

    <section class="spine">
      <div class="spine-text">
        <span class="spine-title">The Quiet Pantry Method</span>
        <span class="spine-author">Marla Voskin</span>
      </div>
    </section>

    <section class="front-cover">
      <div class="salad-photo" role="img" aria-label="Photo of a Greek salad with tomatoes, feta, olives and basil on a dark table"></div>
      <div class="author-photo" role="img" aria-label="Portrait photo of the author"></div>

      <div class="title-block">
        <p class="series-line">The Quiet Pantry Method:</p>
        <h1 class="main-title">Reshape Your Habits<br>Around Meals in<br>Only 30 Days</h1>
      </div>

      <p class="author-name">Marla Voskin</p>
    </section>
  </div>
</body>
</html>
```